Product Line Brochure

Would like to have a bifold brochure for our product line to show to customers. Would like it to incorporate the paragraph description of the product line with the picture, followed by the product listings. I would like the brochure to be clean and modern. We are a specialty chemical manufacturer in NJ area.

```html
<!DOCTYPE html>
<html lang="en">
<head>
<meta charset="utf-8">
<title>Meridian Resin, Inc. – Product Line Brochure</title>
<link href="https://fonts.googleapis.com/css2?family=Oswald:wght@500;600&family=Lato:wght@400;700&display=swap" rel="stylesheet">
<style>
  :root{
    --navy:#1f3a63;
    --navy-deep:#0f2240;
    --blue-mid:#173a70;
    --blue-bright:#0a4ea3;
    --red:#e8141c;
    --yellow-deep:#d9a400;
    --yellow:#f0c419;
    --yellow-light:#f4e04a;
    --paper:#ffffff;
    --panel:#e6e8eb;
    --ink:#222426;
    --stage:#dcdcdc;
  }
  *{margin:0;padding:0;box-sizing:border-box}
  html,body{width:1200px;height:1200px;overflow:hidden;background:var(--stage)}
  .spread{position:absolute;left:0;top:176px;width:1200px;height:848px;background:var(--paper);
    box-shadow:0 10px 30px rgba(0,0,0,.18)}
  .spread-art{position:absolute;inset:0;width:1200px;height:848px}
  .wordmark{position:absolute;background:var(--navy);display:flex;align-items:center;justify-content:center;gap:10px;
    font-family:'Oswald',sans-serif;font-weight:600;color:#fff;letter-spacing:.5px;text-transform:uppercase}
  .wordmark .mark-square{width:14px;height:14px;background:#fff;flex:none}
  .wordmark--front{left:870px;top:56px;width:270px;height:82px;font-size:22px}
  .wordmark--back{left:220px;top:520px;width:210px;height:62px;font-size:16px}
  .wordmark--back .mark-square{width:10px;height:10px}
  .contact{position:absolute;left:170px;top:610px;width:330px;text-align:center;
    font-family:'Lato',sans-serif;font-size:15px;line-height:1.6;color:var(--ink)}
  .contact .label{font-weight:700}
  .tagline{position:absolute;right:28px;top:455px;width:280px;text-align:right;
    font-family:'Oswald',sans-serif;font-weight:600;text-transform:uppercase;line-height:1.02}
  .tagline span{display:block}
  .tagline .navy{color:var(--navy)}
  .tagline .red{color:var(--red)}
  .tagline .lg{font-size:40px}
  .tagline .sm{font-size:24px}
  .tagline .md{font-size:30px}
  .tagline .xl{font-size:46px}
</style>
</head>
<body>
<section class="spread" aria-label="Bifold brochure, back and front cover">
  <svg class="spread-art" viewBox="0 0 1200 848" xmlns="http://www.w3.org/2000/svg">
    <defs>
      <linearGradient id="paint-tones" x1="0" y1="0" x2="1" y2="1">
        <stop offset="0" stop-color="#a07a6a"/>
        <stop offset=".35" stop-color="#c9b05a"/>
        <stop offset=".6" stop-color="#5f7fa0"/>
        <stop offset="1" stop-color="#b98a70"/>
      </linearGradient>
    </defs>
    <!-- back cover -->
    <polygon class="back-photo" role="img" aria-label="Photo of open paint cans in red, yellow and blue with a brush"
      points="0,0 600,0 600,392 0,300" fill="url(#paint-tones)"/>
    <polygon class="back-band" points="0,292 600,380 600,398 0,306" fill="var(--navy)"/>
    <polygon class="back-tri-outer" points="0,306 230,340 0,570" fill="var(--yellow-deep)"/>
    <polygon class="back-tri-mid" points="0,330 190,356 0,530" fill="var(--yellow)"/>
    <polygon class="back-tri-inner" points="0,360 140,378 0,480" fill="var(--yellow-light)"/>
    <!-- front cover -->
    <polygon class="front-red" points="600,0 1000,150 1000,164 600,16" fill="var(--red)"/>
    <polygon class="front-photo" role="img" aria-label="Photo of open paint cans with a brush resting on the blue can"
      points="600,16 1000,164 960,720 600,560" fill="url(#paint-tones)"/>
    <polygon class="front-panel" points="1030,380 1200,372 1200,848 930,848" fill="var(--panel)"/>
    <polygon class="front-tri-dark" points="1150,190 1060,360 1200,362 1200,260" fill="var(--navy-deep)"/>
    <polygon class="front-tri-mid" points="1170,240 1110,356 1200,358 1200,290" fill="var(--blue-mid)"/>
    <polygon class="front-tri-bright" points="1190,280 1150,350 1200,352" fill="var(--blue-bright)"/>
  </svg>

  <div class="wordmark wordmark--back"><span class="mark-square"></span>Meridian Resin, Inc.</div>
  <address class="contact">
    <div><span class="label">Phone :</span> +1 (555) 014 0600</div>
    <div><span class="label">Fax :</span> +1 (555) 014 8442</div>
    <div><span class="label">Address :</span> 218 Harbor Mill Road</div>
    <div>Linden Falls, NJ 07099</div>
    <div><span class="label">Website :</span> www.meridianresin.com</div>
  </address>

  <div class="wordmark wordmark--front"><span class="mark-square"></span>Meridian Resin, Inc.</div>
  <h1 class="tagline">
    <span class="navy lg">To Provide</span>
    <span class="red sm">Effective Solutions</span>
    <span class="navy md">Through Technical</span>
    <span class="navy xl">Innovation</span>
    <span class="red md">And Exemplary Service</span>
  </h1>
</section>
</body>
</html>
```